Business card design needed

I am a small start up business in the mortgage broking industry based in Sydney called 'keys2nest'. I will be providing residential mortgages to first home owners, investors and people looking to refinance. I would like to see designs that use the colors blue, black, and white - same as my logo (see logo design uploaded)

Target Market(s)

My target market is First Home Owners, property investors, and people looking to refinance. The loans I will be providing are for residential property only at this stage, and my clients will predominantly be in the 30-50yr age bracket.

Industry/Entity Type

Residential

Contact Information for Business Card

Owen Partridge
Director/Mobile Mortgage Broker
keys2nest
PO BOX 4287
Westmead NSW 2145
Mb: 0491 862 307
email: owen@keys2nest.com.au

Requirements
Must have
• please use lower case for business name (i.e. keys2nest)

```html
<!DOCTYPE html>
<html lang="en">
<head>
<meta charset="utf-8">
<title>keys2nest business card</title>
<link rel="stylesheet" href="https://fonts.googleapis.com/css2?family=Mulish:wght@300;400;700&family=Kalam:wght@300;400&display=swap">
<style>
  :root {
    --ink: #1a1a1a;
    --brand-blue: #22a9e0;
    --paper: #ffffff;
    --backdrop: #000000;
    --sans: "Mulish", "Century Gothic", sans-serif;
    --script: "Kalam", "Segoe Print", cursive;
  }
  html, body {
    margin: 0;
    padding: 0;
    width: 1200px;
    height: 1000px;
    overflow: hidden;
    background: var(--backdrop);
  }
  .sheet {
    position: absolute;
    left: 186px;
    top: 0;
    width: 827px;
    height: 1000px;
    background: var(--paper);
    font-family: var(--sans);
    color: var(--ink);
  }
  .wordmark {
    position: absolute;
    left: 0;
    width: 100%;
    text-align: center;
    font-family: var(--sans);
    font-weight: 300;
    color: var(--ink);
    letter-spacing: -1px;
    line-height: 1;
    margin: 0;
  }
  .wordmark--front { top: 50px; font-size: 78px; }
  .wordmark--back { top: 836px; font-size: 66px; }

  .person-name {
    position: absolute;
    left: 62px;
    top: 154px;
    margin: 0;
    font-size: 34px;
    font-weight: 700;
    color: var(--brand-blue);
    line-height: 1;
  }
  .person-role {
    position: absolute;
    left: 62px;
    top: 203px;
    margin: 0;
    font-size: 31px;
    font-weight: 400;
    line-height: 1;
  }
  .band {
    position: absolute;
    left: 0;
    width: 100%;
    background: var(--brand-blue);
  }
  .band--contact { top: 255px; height: 189px; }
  .band--pitch { top: 498px; height: 286px; }

  .contact {
    position: absolute;
    left: 62px;
    top: 20px;
    margin: 0;
    font-size: 23px;
    font-weight: 300;
    color: var(--paper);
    line-height: 34px;
    font-style: normal;
  }
  .contact-email {
    position: absolute;
    left: 390px;
    top: 88px;
    margin: 0;
    font-size: 23px;
    font-weight: 300;
    color: var(--paper);
    line-height: 34px;
  }
  .pitch-question {
    position: absolute;
    left: 0;
    top: 104px;
    width: 100%;
    margin: 0;
    text-align: center;
    font-family: var(--script);
    font-weight: 300;
    font-size: 27px;
    line-height: 39px;
    color: var(--ink);
  }
  .pitch-answer {
    position: absolute;
    left: 0;
    top: 196px;
    width: 100%;
    margin: 0;
    text-align: center;
    font-family: var(--script);
    font-weight: 300;
    font-size: 42px;
    line-height: 1;
    color: var(--paper);
  }
  .tagline {
    position: absolute;
    left: 0;
    top: 948px;
    width: 100%;
    margin: 0;
    text-align: center;
    font-size: 37px;
    font-weight: 400;
    line-height: 1;
  }
  .tagline strong {
    color: var(--brand-blue);
    font-weight: 700;
  }
</style>
</head>
<body>
  <main class="sheet">
    <section class="card-front">
      <p class="wordmark wordmark--front">keys2nest</p>
      <h1 class="person-name">Owen Partridge</h1>
      <p class="person-role">Director/Mobile Mortgage Broker</p>
      <div class="band band--contact">
        <address class="contact">
          PO BOX 4287<br>
          Westmead NSW 2145<br>
          m: 0491 862 307
        </address>
        <p class="contact-email">e: owen@keys2nest.com.au</p>
      </div>
    </section>

    <section class="card-back">
      <div class="band band--pitch">
        <p class="pitch-question">Are you looking for your first home, an investment<br>property or to refinance an existing home loan?</p>
        <p class="pitch-answer">You’ve made the right choice...</p>
      </div>
      <p class="wordmark wordmark--back">keys2nest</p>
      <p class="tagline">The number <strong>1 choice</strong> for home loans</p>
    </section>
  </main>
</body>
</html>
```